Lantern Motion for Neighbors Business Cards

I need business cards for staff in a new startup. Our company name is Movrela - we train Tai Chi teachers. But our biggest project is called Lantern Motion for Neighbors - a federal project to put together free Tai Chi classes for Vets all across America. It's a young company, with a spirit of excitement, passion, a desire to do good for others (our Vets) and a modern style and sensibility. In other words, not old-fashioned Asian martial arts theme, but something new.

Industry/Entity Type

Health And Wellness

Contact Information for Business Card

The topic is ancient healing, but the company is the Pembrooks - so I'd like a card design that captures that.

Font styles to use
Sans Serif

Colors

Designer to choose colors to be used in the design.

Requirements
Nice to have
• I've got two logos - one for the company and one for the project. I want to see if we can incorporate them both without it becoming too busy.
Should not have
• Overly old-fashioned yin-yang themes.

```html
<!DOCTYPE html>
<html lang="en">
<head>
<meta charset="utf-8">
<title>Lantern Motion for Neighbors – Business Cards</title>
<link rel="stylesheet" href="https://fonts.googleapis.com/css2?family=Arimo&family=Tenor+Sans&display=swap">
<style>
  :root {
    --bg: #e9e6e1;
    --card: #ffffff;
    --navy: #2b2a6b;
    --red: #e8404f;
    --ink: #111111;
    --rule: #8a8a8a;
    --band-dark: #111111;
  }
  * { margin: 0; padding: 0; box-sizing: border-box; }
  html, body { width: 900px; height: 1200px; overflow: hidden; }
  body { background: var(--bg); position: relative; font-family: "Arimo", Arial, sans-serif; }

  .card {
    position: absolute; left: 80px; width: 734px; height: 428px;
    background: var(--card); border-radius: 24px; overflow: hidden;
    box-shadow: 0 3px 10px rgba(0,0,0,.18);
  }
  .card--front { top: 128px; }
  .card--back { top: 645px; }

  /* front */
  .brand { position: absolute; left: 48px; top: 62px; display: flex; align-items: center; gap: 18px; }
  .brand__dot { width: 96px; height: 96px; border-radius: 50%; border: 5px solid var(--navy); flex: none; }
  .brand__name {
    font-family: "Tenor Sans", sans-serif; color: var(--navy);
    font-size: 29px; line-height: 1.12; width: 230px; letter-spacing: .5px;
  }
  .person { position: absolute; right: 44px; top: 88px; text-align: right; font-family: "Tenor Sans", sans-serif; }
  .person__name { color: var(--navy); font-size: 20px; letter-spacing: .6px; }
  .person__title { color: var(--red); font-size: 16px; letter-spacing: .4px; margin-top: 1px; }

  .divider { position: absolute; left: 48px; right: 46px; top: 254px; border-top: 1.5px solid var(--rule); }

  .address { position: absolute; left: 48px; top: 276px; font-size: 16px; line-height: 23.5px; color: var(--ink); }
  .contact { position: absolute; right: 44px; top: 275px; list-style: none; font-size: 16px; line-height: 23.5px; color: var(--ink); }
  .contact li { display: flex; justify-content: flex-end; align-items: center; gap: 7px; }
  .contact svg { width: 16px; height: 16px; fill: var(--red); flex: none; }

  .stripe { position: absolute; left: 0; right: 0; bottom: 14px; height: 5px; display: flex; }
  .stripe__red { flex: 0 0 366px; background: var(--red); }
  .stripe__navy { flex: 1; background: var(--navy); }

  /* back */
  .mark { position: absolute; left: 0; right: 0; top: 118px; display: flex; justify-content: center; align-items: center; gap: 20px; }
  .mark__dot { width: 110px; height: 110px; border-radius: 50%; background: var(--red); flex: none; }
  .mark__name { font-family: "Tenor Sans", sans-serif; color: var(--red); font-size: 52px; letter-spacing: 1px; }

  .tagline {
    position: absolute; left: 0; right: 0; top: 373px; height: 40px;
    background: linear-gradient(90deg, var(--band-dark) 0%, #5a1a21 45%, var(--red) 100%);
    color: #fff; font-family: "Tenor Sans", sans-serif; font-size: 16.5px;
    display: flex; align-items: center; justify-content: center; letter-spacing: .2px;
  }
</style>
</head>
<body>

<section class="card card--front">
  <div class="brand">
    <span class="brand__dot"></span>
    <span class="brand__name">Lantern Motion for Neighbors</span>
  </div>

  <div class="person">
    <p class="person__name">MARCUS ELLERY</p>
    <p class="person__title">CEO/FOUNDER</p>
  </div>

  <div class="divider"></div>

  <address class="address" style="font-style:normal">
    118 Linden Street SE<br>
    Suite 210, Harbor Falls<br>
    MI 49570
  </address>

  <ul class="contact">
    <li>555 318 4072
      <svg viewBox="0 0 16 16" aria-hidden="true"><path d="M3.6 1.2l2.3 2.6-1.3 1.7c.9 2 2.4 3.6 4.5 4.6l1.7-1.3 2.7 2.3-1.4 2.3C7.3 13.6 2.4 8.7 1.4 2.7z"/></svg>
    </li>
    <li>555 318 4072
      <svg viewBox="0 0 16 16" aria-hidden="true"><path d="M4 1h8v4H4zM1 6h14v6h-3v3H4v-3H1zM5 10v4h6v-4z"/></svg>
    </li>
    <li>marcus@lanternmotion.org
      <svg viewBox="0 0 16 16" aria-hidden="true"><path d="M1 3h14v10H1zM2.5 4.5v.4L8 9l5.5-4.1v-.4z"/></svg>
    </li>
    <li>www.lanternmotion.org
      <svg viewBox="0 0 16 16" aria-hidden="true"><path fill="none" stroke="#e8404f" stroke-width="1.2" d="M8 1.5a6.5 6.5 0 1 0 0 13a6.5 6.5 0 1 0 0-13zM1.5 8h13M8 1.5c-2.4 2.2-2.4 10.8 0 13M8 1.5c2.4 2.2 2.4 10.8 0 13M2.6 4.6h10.8M2.6 11.4h10.8"/></svg>
    </li>
  </ul>

  <div class="stripe"><span class="stripe__red"></span><span class="stripe__navy"></span></div>
</section>

<section class="card card--back">
  <div class="mark">
    <span class="mark__dot"></span>
    <span class="mark__name">Movrela</span>
  </div>
  <p class="tagline">Federal project to put together free Tai Chi classes for Vets all across America.</p>
</section>

</body>
</html>
```